Celebrate February in The Smokies at Maple Hollow Splashpark Lodge

Create something similar to the attached design - can very and be creative but the overall concept is one I would like to recreate
Celebrate February in The Smokies
Maple Hollow logo (at top)
Romantic Rooms, Family Suites, Free Buffet Breakfast included, Indoor Pool and Parkway Convenience
Low Rates!

866.214.5093 MapleHollowLodge.example/

I have attached logos and pictures to use

Target Market(s)

Email customers to entice them to come to the smokies in February ..

Industry/Entity Type

Hospitality

Requirements
Must have
• phone number 866.214.5093
• website MapleHollowLodge.example/
Nice to have
• a romantic feel but not to much so .. families and couples can both enjoy the area in february

```html
<!DOCTYPE html>
<html lang="en">
<head>
<meta charset="utf-8">
<title>Maple Hollow Splashpark Lodge – February Door Hanger</title>
<link rel="stylesheet" href="https://fonts.googleapis.com/css2?family=Roboto+Condensed:wght@400;900&family=Noto+Serif:wght@400;700&family=Arimo:wght@600;700&display=swap">
<style>
  :root {
    --backdrop: #c07ee0;
    --card: #f4f5f7;
    --ink: #111111;
    --brand-navy: #1c2f86;
    --brand-teal: #27a9d8;
    --band: #b3b3b5;
    --photo-wall: #efe0c4;
    --photo-bed: #5d9f8c;
    --photo-floor: #4a4a4a;
  }
  * { margin: 0; padding: 0; box-sizing: border-box; }
  html, body {
    width: 923px;
    height: 1200px;
    overflow: hidden;
    background: var(--backdrop);
  }
  .door-hanger {
    position: absolute;
    left: 396px;
    top: 51px;
    width: 383px;
    height: 1098px;
  }
  .hanger-shape {
    position: absolute;
    inset: 0;
    width: 383px;
    height: 1098px;
  }
  .brand {
    position: absolute;
    top: 42px;
    left: 0;
    width: 383px;
    height: 54px;
    display: flex;
    align-items: center;
    justify-content: center;
    gap: 10px;
  }
  .brand-dot {
    width: 50px;
    height: 50px;
    border-radius: 50%;
    background: var(--brand-teal);
    flex: none;
  }
  .brand-name {
    font-family: "Arimo", Arial, sans-serif;
    font-weight: 600;
    font-size: 19px;
    line-height: 1.2;
    color: var(--brand-navy);
  }
  .headline {
    position: absolute;
    top: 0;
    left: 0;
    width: 383px;
    text-align: center;
    color: var(--ink);
    font-weight: normal;
  }
  .headline-main {
    position: absolute;
    top: 396px;
    left: 0;
    width: 383px;
    font-family: "Roboto Condensed", "Arial Narrow", sans-serif;
    font-weight: 900;
    font-size: 70px;
    line-height: 57px;
    letter-spacing: -0.5px;
    text-transform: uppercase;
  }
  .headline-sub {
    position: absolute;
    top: 512px;
    left: 0;
    width: 383px;
    font-family: "Roboto Condensed", "Arial Narrow", sans-serif;
    font-weight: 400;
    font-size: 40px;
    line-height: 46px;
    letter-spacing: 0.5px;
    text-transform: uppercase;
  }
  .room-photo {
    position: absolute;
    top: 560px;
    left: 30px;
    width: 319px;
    height: 178px;
    background: linear-gradient(180deg, var(--photo-wall) 0%, var(--photo-wall) 55%, var(--photo-bed) 72%, var(--photo-floor) 100%);
  }
  .amenities {
    position: absolute;
    top: 763px;
    left: 36px;
    width: 311px;
    text-align: center;
    font-family: "Noto Serif", Georgia, serif;
    font-size: 21px;
    line-height: 30.5px;
    letter-spacing: 0.6px;
    color: var(--ink);
  }
  .rate-callout {
    position: absolute;
    top: 924px;
    left: 0;
    width: 383px;
    line-height: 28px;
    text-align: center;
    font-family: "Noto Serif", Georgia, serif;
    font-weight: 700;
    font-size: 20px;
    letter-spacing: 1px;
    color: var(--ink);
  }
  .contact {
    position: absolute;
    top: 982px;
    left: 8px;
    width: 383px;
    text-align: center;
    font-family: "Arimo", Arial, sans-serif;
    font-weight: 700;
    color: var(--ink);
  }
  .contact-phone {
    font-size: 41px;
    line-height: 46px;
  }
  .contact-web {
    font-size: 21px;
    line-height: 26px;
  }
</style>
</head>
<body>
  <div class="door-hanger">
    <svg class="hanger-shape" viewBox="0 0 383 1098" aria-hidden="true">
      <defs>
        <mask id="hanger-cutout">
          <rect x="0" y="0" width="383" height="1098" fill="#fff"/>
          <circle cx="195" cy="235" r="55" fill="#000"/>
          <polygon points="-2,157 117,157 150,190 150,290 121,318 -2,376" fill="#000"/>
        </mask>
        <clipPath id="hanger-clip">
          <rect x="0" y="0" width="383" height="1098" rx="11"/>
        </clipPath>
      </defs>
      <g mask="url(#hanger-cutout)" clip-path="url(#hanger-clip)">
        <rect x="0" y="0" width="383" height="1098" fill="var(--card)"/>
        <rect x="0" y="1066" width="383" height="32" fill="var(--band)"/>
      </g>
    </svg>

    <div class="brand">
      <span class="brand-dot"></span>
      <span class="brand-name">Maple Hollow<br>Splashpark Lodge</span>
    </div>

    <h1 class="headline">
      <div class="headline-main">Celebrate<br>February</div>
      <div class="headline-sub">in the Smokies</div>
    </h1>

    <div class="room-photo" role="img" aria-label="Photo of a bright lodge suite with vaulted ceiling, tall window, bed with teal spread and a white soaking tub"></div>

    <p class="amenities">Romantic Rooms, Family Suites, Free Buffet Breakfast included, Indoor Pool and Parkway Convenience</p>

    <p class="rate-callout">LOW RATES !</p>

    <div class="contact">
      <div class="contact-phone">866.214.5093</div>
      <div class="contact-web">MapleHollowLodge.example</div>
    </div>
  </div>
</body>
</html>
```